Diagramm/Grafik zur Darstellung einer Formel
Zielgruppe
Das Unternehmen ist in der Unternehmensberatung tätig und beschäftigt sich mit der Analyse von IT-In- und Outsourcing.
Zielgruppe: Entscheider / Höheres Management / Round Table
Aufgabenstellung
Es wurde für die Bewertung des bestehenden Outsourcing eine Formel entwickelt, welche es ermöglicht einerseits die Stärken
und Schwächen und andererseits die Entwicklung und Vorteilhaftigkeit der Kosten für die nächsten Jahre zu prognostizieren.
Der Name der Formel ist "MIRAX-P Methode" (Strategie, Technologie, Organisation, Qualität und Kosten)
Die Formel ist aufgebaut aus 5 Sektoren, unter welchem jeweils 3-8 Faktoren untergeordnet sind. (siehe IMG_1159)
Die Zuordnung der Faktoren zu Sektoren (siehe SektorenFaktoren.pdf) ist variabel, aus welchem Grund unter jedem Sektor 3-8 Faktoren unterordnenbar sein sollten.
Grundsätzlich findet die Auswertung aus dem Vergleich von Kosten + Risiken - Chancen jeweils von Outsourcing und Insourcing statt. (siehe IMG_1190)
Ziel ist es, eine Darstellung der Sektoren und Faktoren sowie der Formel zu finden, welche:
a) die Abhängigkeit von den Faktoren zu den Sektoren darstellt
b) die Formel darstellt
c) sich als Ganzes oder in Teilen für diverse Unterlagen verwenden lässt (bspw. .pptx, .pdf, etc.)
--> es ist geplant diese Darstellung bspw. als Ganzes oder in Teilen in eine PowerPoint-Präsentation zu integrieren
Diese Aufgabenstellung ist ein erster Versuch mittels der Plattform pixelhafen.de Aufträge zu vergeben.
Bei Erfolg sind Anschlussaufträge geplant.
WICHTIG: Alle Anhänge diesen lediglich zur Darstellung der Zusammenhänge, sollen aber keinerlei design vorgeben!

```html
<!DOCTYPE html>
<html lang="de">
<head>
<meta charset="utf-8">
<title>MIRAX-P Methode</title>
<link href="https://fonts.googleapis.com/css2?family=Carlito:wght@400;700&display=swap" rel="stylesheet">
<style>
  :root {
    --navy-top: #5479a3;
    --navy-bottom: #2f4d72;
    --orange: #e2500f;
    --orange-dark: #9a2e08;
    --band: #dce6f2;
    --frame: #5b7aa6;
    --label: #1f3555;
    --factor-blue: #2e5a96;
    --factor-grey: #7f7f7f;
    --white: #ffffff;
  }
  * { margin: 0; padding: 0; box-sizing: border-box; }
  html, body { width: 1200px; height: 900px; overflow: hidden; background: var(--white); }
  body { font-family: "Carlito", "Calibri", sans-serif; position: relative; }
  .shapes { position: absolute; left: 0; top: 0; }
  .title {
    position: absolute; top: 12px; left: 0; width: 1200px; text-align: center;
    color: var(--white); font-weight: 700; font-size: 44px; letter-spacing: 0.5px;
  }
  .side-heading {
    position: absolute; top: 90px; width: 400px; text-align: center;
    color: var(--orange); font-weight: 700; font-size: 38px; letter-spacing: 0.5px;
  }
  .side-heading.out { left: 90px; }
  .side-heading.in { left: 709px; }
  .sector-label {
    position: absolute; height: 114px; display: flex; align-items: center;
    color: var(--label); font-size: 25px;
  }
  .sector-label.left { left: 89px; }
  .sector-label.right { right: 99px; }
  .factors {
    position: absolute; left: 280px; width: 630px; height: 114px;
    display: flex; flex-direction: column; justify-content: center; align-items: center;
    font-size: 18.5px; line-height: 24px; text-align: center;
  }
  .factors span { margin: 0 8px; }
  .f-blue { color: var(--factor-blue); }
  .f-grey { color: var(--factor-grey); }
  .formula {
    position: absolute; top: 794px; height: 53px; width: 511px;
    background: linear-gradient(90deg, var(--orange), var(--orange-dark));
    color: var(--white); font-weight: 700; font-size: 31px;
    display: flex; align-items: center; justify-content: center; letter-spacing: 0.3px;
  }
  .formula.out { left: 62px; }
  .formula.in { left: 619px; }
</style>
</head>
<body>
<svg class="shapes" width="1200" height="900" viewBox="0 0 1200 900">
  <defs>
    <linearGradient id="headerGrad" x1="0" y1="0" x2="0" y2="1">
      <stop offset="0" stop-color="#5a7fa9"/>
      <stop offset="1" stop-color="#2d4a6e"/>
    </linearGradient>
    <linearGradient id="badgeGrad" x1="0" y1="0" x2="1" y2="1">
      <stop offset="0" stop-color="#ec5a14"/>
      <stop offset="1" stop-color="#a8330a"/>
    </linearGradient>
  </defs>
  <rect x="0" y="0" width="1200" height="109" fill="url(#headerGrad)"/>
  <polygon points="14,81 544,81 572,109 628,109 656,81 1186,81 1186,130 14,130" fill="#ffffff"/>
  <circle cx="600" cy="105" r="25" fill="#ffffff"/>
  <circle cx="600" cy="105" r="22" fill="url(#badgeGrad)"/>

  <g stroke="#5b7aa6" stroke-width="1.3">
    <!-- Strategie -->
    <rect x="61" y="163" width="1070" height="114" fill="#dce6f2" stroke="none"/>
    <polygon points="61,163 250,163 278,220 250,277 61,277" fill="#dce6f2"/>
    <polygon points="940,164 1131,164 1131,277 940,277 912,220" fill="#dce6f2"/>
    <!-- Technologie -->
    <polygon points="61,286 250,286 278,343 250,400 61,400" fill="#ffffff"/>
    <polygon points="940,287 1131,287 1131,400 940,400 913,343" fill="#ffffff"/>
    <!-- Organisation -->
    <rect x="60" y="409" width="1071" height="113" fill="#dce6f2" stroke="none"/>
    <polygon points="60,409 249,409 277,466 249,522 60,522" fill="#dce6f2"/>
    <polygon points="940,410 1130,410 1130,522 940,522 912,466" fill="#dce6f2"/>
    <!-- Qualität -->
    <polygon points="61,531 250,531 278,588 250,645 61,645" fill="#ffffff"/>
    <polygon points="940,532 1131,532 1131,645 940,645 913,588" fill="#ffffff"/>
    <!-- Kosten -->
    <rect x="62" y="653" width="1069" height="114" fill="#dce6f2" stroke="none"/>
    <polygon points="62,653 251,653 279,710 251,767 62,767" fill="#dce6f2"/>
    <polygon points="940,654 1131,654 1131,767 940,767 913,710" fill="#dce6f2"/>
  </g>
</svg>

<div class="title">MIRAX-P Methode</div>
<div class="side-heading out">OUTSOURCING</div>
<div class="side-heading in">INSOURCING</div>

<div class="sector-label left" style="top:163px">Strategie</div>
<div class="sector-label right" style="top:164px">Strategie</div>
<div class="factors" style="top:163px">
  <div><span class="f-blue">Komparativer Konkurrenzvorteil</span><span class="f-grey">Kernkompetenz</span></div>
  <div><span class="f-grey">Wertschöpfungstiefe</span><span class="f-blue">Marktbewegung</span></div>
  <div><span class="f-blue">Marktein- / -austrittsstrategie</span></div>
  <div><span class="f-grey">Sourcing- / Vendorstrategie</span><span class="f-blue">Risikoabsicherung</span><span class="f-grey">Ungewissheit</span></div>
</div>

<div class="sector-label left" style="top:286px">Technologie</div>
<div class="sector-label right" style="top:287px">Technologie</div>
<div class="factors" style="top:286px">
  <div><span class="f-blue">Innovationsrate</span><span class="f-grey">Synergien</span></div>
  <div><span class="f-grey">Portfolio-Erweiterung</span><span class="f-blue">Best-Practices</span></div>
</div>

<div class="sector-label left" style="top:409px">Organisation</div>
<div class="sector-label right" style="top:409px">Organisation</div>
<div class="factors" style="top:409px">
  <div><span class="f-blue">Wissen</span><span class="f-grey">Kommunikation</span></div>
  <div><span class="f-grey">Umsetzungsgeschwindigkeit</span><span class="f-blue">Flexibilität</span></div>
  <div><span class="f-blue">Skalierbarkeit</span><span class="f-grey">Time-to-Market</span></div>
  <div><span class="f-blue">Organisationstransformation</span></div>
</div>

<div class="sector-label left" style="top:531px">Qualität</div>
<div class="sector-label right" style="top:532px">Qualität</div>
<div class="factors" style="top:531px">
  <div><span class="f-blue">Kontroll- und Prüfaufwände</span><span class="f-grey">Compliance (legal)</span></div>
  <div><span class="f-grey">Sprach- /Kulturbarrieren</span><span class="f-blue">Distanz / Nähe</span></div>
</div>

<div class="sector-label left" style="top:653px">Kosten</div>
<div class="sector-label right" style="top:654px">Kosten</div>
<div class="factors" style="top:653px">
  <div><span class="f-blue">Management-Kosten</span><span class="f-grey">Vertragsänderungs- / -</span></div>
  <div><span class="f-grey">verwaltungskosten</span><span class="f-blue">Cash Flow</span><span class="f-grey">Return-on-Invest</span></div>
  <div><span class="f-blue">fixe vs. Variable Kosten</span><span class="f-grey">Tax</span></div>
</div>

<div class="formula out">Kosten + Risiken - Chancen =</div>
<div class="formula in">Kosten + Risiken - Chancen =</div>
</body>
</html>
```